Swimming Pool Service Website needed!!!

Hi Everyone! Thanks for looking at my contest. I PROMISE to provide excellent feedback during this process.

I am starting a new swimming pool business cleaning company in San Diego, California and would like your help in making it similar to one of these two websites that are already functioning.

http://www.brightlagoonworks.example/services-repair.html

http://tidemarkaquacare.example/commercial-pool-cleaning.php

I like these two because they are easy to read, classy, sophisticated and have nice pictures of really clean & clear pools.

I really like the blue on white color format.

I do not have a logo, but the name of my company is GLIMMERWAVE POOL SERVICE.

My tag line is: Water so pure, it sparkles like a summer sky. (does not need to have the quotes around "in"...maybe just italics for this word IN?) You decide for me.

I would like to have a logo designed that incorporates some sort of easy to read letters. I do not want cursive (handwriting) letters. I thought about having a "reflection" of letters (mirror image), but think that this will be hard to read from far away. Maybe you can surprise me and come up with an idea that works using the a mirror image....but I'm not sure. I was leaning toward plain old BLOCK letters as I think it would be easy to read on my truck.

I would like to have 5 pages on my website:
1) Home
2) About Us (Know Your Poolman) / Why Hire Us
3) Services Offered
4) FAQ's
5) Contact

I am looking for a fully-functioning website (coded). Upon selection of the design winner, I am offering to increase the budget/payment by $100-$125 for the coding of all the pages. So anyone looking at participating in this contest, should be willing and able to provide the coding to the webpages that i've requested.

Target Market(s)

Upper middle-class homeowners who have a pool

Industry/Entity Type

Pool Service

Number of Pages Required

5+ page

Font styles to use
Serif

Colors
0455a3
3276b5
85acd3
85cae6
ffffff
33a6d7
0592cd

Requirements
Must have
• The Home page must have this picture highlighted in the top of the page:
• http://www.mesawaterpro.example/
• Must have pictures of some high-end pools. Any that you can find on the internet are wonderful.
• Must have a table on the right of the home page that mentions the service areas that we go to:
• • Carmel Valley (92130)
• • Del Mar (92014)
• • Rancho Santa Fe (92067)
• • Solana Beach (92075)
• • Santaluz (92127)
• • Cardiff (92007)
• • Encinitas (92024)
• • Carlsbad (92009, 92008)
• • La Jolla (92037)
• • Pacific Beach (92109)
• • Mira Mesa (92126)
• • Sorrento Valley (92121)
• • Clairemont (92117)
• • Rancho Bernardo (92127, 92128)
• • Rancho Penasquitos (92129)
• • Poway (92064)
• •
Nice to have
• Maybe incorporate some pictures of some kids (or families) playing in pools on the Why Hire Us page?
• I also like the feel of this website, but posting this page just for reference so you can get a feel more of what I like:
• http://www.crestlinepool.example/
• I like the FAQ's page from this website. I like how you can click on the question and then it pops up with the answer. http://www.dunewoodpoolcare.example/pool-spa-fountain-faqs/

```html
<!DOCTYPE html>
<html lang="en">
<head>
<meta charset="utf-8">
<title>Glimmerwave Pool Service</title>
<link rel="stylesheet" href="https://fonts.googleapis.com/css2?family=Open+Sans:wght@400;600;700&family=Sansita:ital,wght@0,800;1,800;1,900&display=swap">
<style>
  :root{
    --navy:#0455a3;
    --blue:#3276b5;
    --sky:#85acd3;
    --pale:#85cae6;
    --band:#33a6d7;
    --ocean:#0592cd;
    --ink:#1f3550;
    --muted:#6f7c88;
    --nav:#0455a3;
    --line:#d3e2ef;
    --white:#ffffff;
  }
  *{box-sizing:border-box;margin:0;padding:0}
  html,body{width:686px;height:1200px;overflow:hidden;background:var(--white)}
  body{position:relative;font-family:"Open Sans",Arial,sans-serif;color:var(--ink)}
  .abs{position:absolute}

  /* top navigation */
  .topnav{left:0;top:0;width:686px;height:15px;background:var(--nav);display:flex;justify-content:center;gap:22px;align-items:center}
  .topnav a{color:var(--white);font-size:5.5px;letter-spacing:.6px;text-decoration:none;font-weight:600}

  /* brand */
  .brand{left:0;top:34px;width:686px;display:flex;justify-content:center;align-items:center;gap:8px}
  .brand-dot{width:30px;height:30px;border-radius:50%;background:var(--navy)}
  .brand-name{font-family:"Sansita",Georgia,serif;font-weight:800;font-size:19px;color:var(--navy);line-height:1}
  .brand-tag{font-family:"Sansita",Georgia,serif;font-weight:800;font-size:8.5px;color:var(--navy);margin-top:3px}

  /* blue bands with zigzag edges */
  .band{left:0;width:686px;background:var(--band)}
  .zig-top,.zig-bottom{position:absolute;left:0;width:100%;height:7px;background-size:12px 12px;background-repeat:repeat-x}
  .zig-top{top:-7px;background-image:linear-gradient(45deg,var(--band) 6px,transparent 0),linear-gradient(-45deg,var(--band) 6px,transparent 0);background-position:left bottom}
  .zig-bottom{bottom:-7px;background-image:linear-gradient(135deg,var(--band) 6px,transparent 0),linear-gradient(-135deg,var(--band) 6px,transparent 0);background-position:left top}
  .hero-band{top:272px;height:392px}
  .foot-band{top:984px;height:216px}

  /* hero */
  .hero-photo{position:absolute;border-radius:50%;border:3px solid var(--white)}
  .photo-left{left:78px;top:108px;width:190px;height:190px;background:radial-gradient(circle at 40% 40%,#bfe7f3,#3fa5d0 60%,#1d6f9f)}
  .photo-right{left:412px;top:100px;width:200px;height:200px;background:radial-gradient(circle at 55% 45%,#d9f1f7,#5bb7dc 55%,#2f7fb5)}
  .photo-main{left:192px;top:98px;width:302px;height:302px;background:linear-gradient(160deg,#a9dcef 0%,#4fb2dc 45%,#137fbd 100%)}
  .hero-title{left:0;top:224px;width:686px;text-align:center;font-family:"Sansita",Georgia,serif;font-style:italic;font-weight:900;font-size:76px;color:var(--white);line-height:1;letter-spacing:1px}
  .hero-sub{left:0;top:300px;width:686px;text-align:center;font-family:"Sansita",Georgia,serif;font-style:italic;font-weight:800;font-size:14px;color:#fdf6c8;letter-spacing:.5px}

  /* features */
  .features{left:92px;top:420px;width:503px;display:grid;grid-template-columns:repeat(4,1fr)}
  .feature{text-align:center}
  .feature-photo{width:112px;height:112px;border-radius:50%;margin:0 auto;border:3px solid var(--white)}
  .f1{background:radial-gradient(circle at 45% 45%,#8fd4ee,#1f86c2)}
  .f2{background:radial-gradient(circle at 50% 60%,#7cc9ec,#0a5fa7)}
  .f3{background:linear-gradient(150deg,#d6eef6,#55b4dc 55%,#1b77b3)}
  .f4{background:linear-gradient(180deg,#bfe0ec 0%,#8cc4a6 45%,#3d9bc9 100%)}
  .feature h3{font-family:"Sansita",Georgia,serif;font-weight:800;font-size:8.5px;letter-spacing:.4px;color:var(--white);margin-top:17px}
  .feature p{font-size:6px;line-height:1.55;color:#eef8fd;width:100px;margin:7px auto 0}
  .feature a{display:inline-block;margin-top:15px;font-size:5.5px;font-weight:700;color:var(--navy);text-decoration:underline;letter-spacing:.4px}

  /* welcome + consultation */
  .section-title{font-family:"Sansita",Georgia,serif;font-style:italic;font-weight:800;font-size:19px;color:var(--navy);letter-spacing:.5px}
  .welcome{left:92px;top:686px;width:215px}
  .welcome-lead{margin-top:18px;font-family:"Sansita",Georgia,serif;font-style:italic;font-weight:800;font-size:9.5px;line-height:1.45;color:var(--ocean)}
  .welcome p{font-size:6px;line-height:1.7;color:var(--muted);margin-top:10px}

  .consult{left:350px;top:686px;width:245px}
  .consult-form{margin-top:14px}
  .field{height:19px;border-bottom:1px solid var(--line);display:flex;align-items:flex-end;padding-bottom:3px;font-size:6px;color:var(--ink)}
  .submit{margin:10px 0 0 auto;width:68px;height:17px;background:var(--navy);color:var(--white);font-size:5.5px;font-weight:700;letter-spacing:.4px;display:flex;align-items:center;justify-content:center}

  /* service areas */
  .areas{left:350px;top:876px;width:245px}
  .areas-title{font-family:"Sansita",Georgia,serif;font-style:italic;font-weight:800;font-size:11px;color:var(--navy);letter-spacing:.4px;padding-bottom:3px;border-bottom:2px solid var(--band)}
  .areas-table{width:100%;border-collapse:collapse;margin-top:3px;font-size:5.5px;line-height:1}
  .areas-table td{height:9px;border-bottom:1px solid var(--line);color:var(--ink)}
  .areas-table td.zip{color:var(--ocean);font-weight:600;padding-right:6px}

  .slide-arrow{left:676px;top:782px;width:18px;height:18px;border-radius:50%;background:var(--navy)}

  /* footer */
  .foot-kicker{left:0;top:1000px;width:686px;text-align:center;font-size:6px;letter-spacing:1px;color:var(--white);font-weight:600}
  .foot-title{left:0;top:1006px;width:686px;text-align:center;font-family:"Sansita",Georgia,serif;font-style:italic;font-weight:900;font-size:84px;line-height:1;color:var(--white);letter-spacing:2px}
  .foot-sub{left:0;top:1094px;width:686px;text-align:center;font-size:6px;letter-spacing:1px;color:var(--white);font-weight:700}
  .socials{left:0;top:1110px;width:686px;display:flex;justify-content:center;gap:5px}
  .socials span{width:13px;height:13px;border-radius:50%;background:var(--navy)}
  .foot-address{left:0;top:1134px;width:686px;text-align:center;font-size:5.5px;line-height:1.6;color:var(--white)}
  .copyright{left:0;top:1172px;width:686px;text-align:center;font-size:6px;color:var(--white)}
</style>
</head>
<body>

<nav class="abs topnav">
  <a href="#">HOME</a><a href="#">ABOUT</a><a href="#">PRODUCTS</a><a href="#">BLOG</a><a href="#">CONTACT</a>
</nav>

<header class="abs brand">
  <span class="brand-dot"></span>
  <div>
    <div class="brand-name">GLIMMERWAVE POOL SERVICE</div>
    <div class="brand-tag">Water so pure, it sparkles like a summer sky.</div>
  </div>
</header>

<div class="abs band hero-band"><span class="zig-top"></span><span class="zig-bottom"></span></div>

<div class="hero-photo photo-left" role="img" aria-label="Photo of a clear backyard swimming pool"></div>
<div class="hero-photo photo-right" role="img" aria-label="Photo of a luxury pool with turquoise water"></div>
<div class="hero-photo photo-main" role="img" aria-label="Photo of sparkling blue pool water"></div>
<h1 class="abs hero-title">CLEAN POOL</h1>
<div class="abs hero-sub">SAVING YOUR ENERGY AND MONEY!</div>

<section class="abs features">
  <article class="feature">
    <div class="feature-photo f1" role="img" aria-label="Photo of a swim spa"></div>
    <h3>SWIM SPA REPAIR</h3>
    <p>Fast repair for pumps, heaters and jets, done right the first time.</p>
    <a href="#">READ MORE</a>
  </article>
  <article class="feature">
    <div class="feature-photo f2" role="img" aria-label="Photo of a pool seen from above"></div>
    <h3>KIT AND CARE</h3>
    <p>Weekly care keeps your water balanced, clear and safe all year.</p>
    <a href="#">READ MORE</a>
  </article>
  <article class="feature">
    <div class="feature-photo f3" role="img" aria-label="Photo of a pool waterfall feature"></div>
    <h3>PET FRIENDLY</h3>
    <p>Gentle treatments that are kind to pets, kids and your family.</p>
    <a href="#">READ MORE</a>
  </article>
  <article class="feature">
    <div class="feature-photo f4" role="img" aria-label="Photo of a garden pool with palm trees"></div>
    <h3>HOME SYSTEMS</h3>
    <p>Filters, lights and automation set up for easy daily use.</p>
    <a href="#">READ MORE</a>
  </article>
</section>

<section class="abs welcome">
  <h2 class="section-title">WELCOME</h2>
  <div class="welcome-lead">WE PROVIDE SERVICES FOR ALL SIZES OF COMMERCIAL OR COMMUNITY SWIMMING POOLS</div>
  <p>Our local team cleans, tests and balances every pool we visit. We treat each backyard like our own, with careful brushing, skimming and filter checks so your water stays bright and inviting.</p>
  <p>From small home pools to large community sites, we keep a steady schedule you can count on.</p>
</section>

<section class="abs consult">
  <h2 class="section-title">REQUEST A CONSULTATION</h2>
  <form class="consult-form">
    <div class="field">Name</div>
    <div class="field">Email</div>
    <div class="field">Phone</div>
    <div class="field">Zip</div>
    <div class="field">Comments</div>
    <div class="submit">SUBMIT REQUEST</div>
  </form>
</section>

<section class="abs areas">
  <h2 class="areas-title">SERVICE AREAS</h2>
  <table class="areas-table">
    <tr><td>Carmel Valley</td><td class="zip">92130</td><td>Encinitas</td><td class="zip">92024</td></tr>
    <tr><td>Del Mar</td><td class="zip">92014</td><td>Carlsbad</td><td class="zip">92009, 92008</td></tr>
    <tr><td>Rancho Santa Fe</td><td class="zip">92067</td><td>La Jolla</td><td class="zip">92037</td></tr>
    <tr><td>Solana Beach</td><td class="zip">92075</td><td>Pacific Beach</td><td class="zip">92109</td></tr>
    <tr><td>Santaluz</td><td class="zip">92127</td><td>Mira Mesa</td><td class="zip">92126</td></tr>
    <tr><td>Cardiff</td><td class="zip">92007</td><td>Sorrento Valley</td><td class="zip">92121</td></tr>
    <tr><td>Clairemont</td><td class="zip">92117</td><td>Rancho Bernardo</td><td class="zip">92127, 92128</td></tr>
    <tr><td>Poway</td><td class="zip">92064</td><td>Rancho Penasquitos</td><td class="zip">92129</td></tr>
  </table>
</section>

<svg class="abs slide-arrow" viewBox="0 0 18 18" aria-hidden="true"><path d="M7 5l-4 4 4 4" fill="none" stroke="#fff" stroke-width="1.6"/></svg>

<footer>
  <div class="abs band foot-band"><span class="zig-top"></span></div>
  <div class="abs foot-kicker">SPARKLING WATER EVERY WEEK</div>
  <div class="abs foot-title">POOL</div>
  <div class="abs foot-sub">CLEANING</div>
  <div class="abs socials"><span></span><span></span><span></span><span></span><span></span></div>
  <div class="abs foot-address">1200 Harbor Lane, San Diego, CA 92130<br>(555) 014-2290<br>hello@glimmerwave.example</div>
  <div class="abs copyright">© All Rights Reserved | Privacy Policy</div>
</footer>

</body>
</html>
```